Contemporary update for a market leader in foodservice distribution

KORVELT is a market leader in foodservice distribution nationwide.
We have recently adopted a new look and feel for our flagship foodservice rewards programme, and we're looking to have our business cards reflect our new aesthetic. Below is a link to our new rewards website to give you a general idea on the look we're after. https://korveltperks.com.au/

Industry/Entity Type

Distribution

Contact Information for Business Card

Must have space for contact name, position, company name and ABN, address, phone number and direct number, fax, email, and web address.

Font styles to use
Serif
Sans Serif

Requirements
Must have
• We'd like a landscape design, with our 'Tip of the Peak' logo incorporated on either the front or the back of the card. The overall design should be contemporary and professional.
Nice to have
• I have included both the full colour and white version of our company logo - our preference is to have the company logo one solid colour (white, or a shade of grey) although we're also open to designs including the full colour logo. If you are able to incorporate a small Facebook and LinkedIn logo, please do so.
Should not have
• Should not have an over-complicated design. No images of globes, or food.

```html
<!DOCTYPE html>
<html lang="en">
<head>
<meta charset="utf-8">
<title>KORVELT Business Card</title>
<link rel="stylesheet" href="https://fonts.googleapis.com/css2?family=Marcellus&family=Open+Sans:wght@400;600&display=swap">
<style>
  :root {
    --brand-green: #0b8a5e;
    --accent-yellow: #f2e400;
    --paper-white: #ffffff;
    --ink-black: #1a1a1a;
    --backdrop: #e9e7e3;
    --shadow: rgba(0, 0, 0, 0.18);
  }
  * { box-sizing: border-box; margin: 0; padding: 0; }
  html, body {
    width: 1200px; height: 900px; overflow: hidden;
    background: var(--backdrop);
    font-family: "Open Sans", Arial, sans-serif;
  }
  .card {
    position: absolute; left: 250px;
    width: 700px; height: 400px;
    box-shadow: 0 6px 18px var(--shadow);
    overflow: hidden;
  }
  .card-back { top: 35px; background: var(--brand-green); }
  .card-front { top: 465px; background: var(--paper-white); }
  .card-shapes { position: absolute; inset: 0; }

  .wordmark {
    position: absolute; display: flex; align-items: center; gap: 20px;
  }
  .wordmark-dot {
    width: 60px; height: 60px; border-radius: 50%;
    border: 5px solid currentColor;
  }
  .wordmark-name {
    font-family: "Marcellus", Georgia, serif;
    font-size: 74px; letter-spacing: 3px; line-height: 1;
  }
  .card-back .wordmark { left: 160px; top: 120px; color: var(--paper-white); }
  .card-front .wordmark { left: 200px; top: 50px; }
  .card-front .wordmark-dot { color: var(--brand-green); }
  .card-front .wordmark-name { color: var(--ink-black); }

  .award-badge {
    position: absolute; left: 314px; top: 275px;
    width: 72px; height: 72px; border-radius: 50%;
    background: var(--paper-white);
  }

  .contact-person {
    position: absolute; right: 370px; top: 250px;
    text-align: right; color: var(--paper-white);
  }
  .person-name { font-size: 26px; font-weight: 600; line-height: 1.2; }
  .person-role { font-size: 18px; line-height: 1.3; margin-bottom: 12px; }
  .person-address { font-size: 19px; line-height: 1.35; }

  .contact-list {
    position: absolute; left: 420px; top: 212px;
    list-style: none; color: var(--paper-white);
    font-size: 17px;
  }
  .contact-list li {
    display: flex; align-items: center; gap: 9px; height: 27px;
  }
  .contact-icon {
    width: 18px; height: 18px; background: var(--paper-white);
    border-radius: 2px; display: flex; align-items: center; justify-content: center;
  }
  .contact-icon svg { width: 13px; height: 13px; fill: var(--brand-green); stroke: var(--brand-green); }
</style>
</head>
<body>

<section class="card card-back" aria-label="Card back">
  <div class="wordmark">
    <span class="wordmark-dot"></span>
    <span class="wordmark-name">KORVELT</span>
  </div>
  <div class="award-badge" role="img" aria-label="Tip of the Peak programme badge"></div>
</section>

<section class="card card-front" aria-label="Card front">
  <svg class="card-shapes" viewBox="0 0 700 400" width="700" height="400" aria-hidden="true">
    <polygon points="0,266 700,130 700,137 0,273" fill="var(--accent-yellow)"/>
    <polygon points="0,282 700,146 700,400 0,400" fill="var(--brand-green)"/>
  </svg>

  <div class="wordmark">
    <span class="wordmark-dot"></span>
    <span class="wordmark-name">KORVELT</span>
  </div>

  <div class="contact-person">
    <p class="person-name">John Smith</p>
    <p class="person-role">Managing Director</p>
    <p class="person-address">1234, Address GoesHere<br>Country, 12345</p>
  </div>

  <ul class="contact-list">
    <li>
      <span class="contact-icon"><svg viewBox="0 0 16 16"><path d="M3 2h3l1 4-2 1c1 2 2 3 4 4l1-2 4 1v3c0 1-1 1-1 1C7 14 2 9 2 3c0 0 0-1 1-1z" stroke="none"/></svg></span>
      123-456-7890
    </li>
    <li>
      <span class="contact-icon"><svg viewBox="0 0 16 16"><rect x="2" y="6" width="12" height="8" stroke="none"/><rect x="4" y="2" width="8" height="5" fill="none" stroke-width="1.5"/></svg></span>
      123-456-7890
    </li>
    <li>
      <span class="contact-icon"><svg viewBox="0 0 16 16"><rect x="1.5" y="3.5" width="13" height="9" fill="none" stroke-width="1.5"/><path d="M2 4l6 5 6-5" fill="none" stroke-width="1.5"/></svg></span>
      info@youremail.com
    </li>
    <li>
      <span class="contact-icon"><svg viewBox="0 0 16 16"><path d="M7 9l3-3M6 7L4 9a2 2 0 003 3l2-2M10 9l2-2a2 2 0 00-3-3L7 6" fill="none" stroke-width="1.6"/></svg></span>
      www.yourweb.com
    </li>
  </ul>
</section>

</body>
</html>
```